Business card design needed

We are a wine business involved in winemaking, broking and packaging on behalf of clients globally with the majority being Asian. The design should be quite traditional and classic with some red used, font used should be easily read.

Target Market(s)

Trade customers other business owners

Industry/Entity Type

Business

Contact Information for Business Card

Rosalind Thwaite
Meridale Wine Collective
PO Box 738, Fenwick Vale
South Australia 5187
Phone: +61 (0)455 982 317
Email: kvcellars@brightmail.example

Logo styles of interest
Lettermark Logo

```html
<!DOCTYPE html>
<html lang="en">
<head>
<meta charset="utf-8">
<title>Rosalind Thwaite – Business Card</title>
<link rel="stylesheet" href="https://fonts.googleapis.com/css2?family=Cinzel:wght@400;500&family=Tinos&display=swap">
<style>
  :root {
    --page-bg: #2b2b2b;
    --card-bg: #ffffff;
    --card-shade: #ececec;
    --wine: #8c1650;
    --wine-light: #b5226a;
    --text-grey: #5a5a5a;
  }
  * { margin: 0; padding: 0; box-sizing: border-box; }
  html, body {
    width: 1200px;
    height: 900px;
    overflow: hidden;
    background: var(--page-bg);
  }
  .card {
    position: absolute;
    left: 100px;
    top: 164px;
    width: 1000px;
    height: 572px;
    background: linear-gradient(160deg, var(--card-bg) 40%, var(--card-shade) 100%);
    overflow: hidden;
  }
  .edge-band {
    position: absolute;
    top: 0;
    right: 0;
    width: 84px;
    height: 100%;
    background: linear-gradient(90deg, var(--wine-light), var(--wine));
  }
  .pour-artwork {
    position: absolute;
    left: 0;
    top: 110px;
    width: 290px;
    height: 462px;
  }
  .contact {
    position: absolute;
    right: 150px;
    top: 56px;
    text-align: right;
    font-family: "Tinos", "Times New Roman", serif;
    color: var(--text-grey);
  }
  .contact__name {
    font-family: "Cinzel", "Trajan Pro", serif;
    font-weight: 500;
    font-size: 42px;
    letter-spacing: 1px;
    color: var(--wine);
    margin-bottom: 22px;
  }
  .contact__company {
    font-size: 34px;
    line-height: 1.15;
  }
  .contact__line {
    font-size: 30px;
    line-height: 1.2;
  }
  .contact__line--gap { margin-top: 28px; }
</style>
</head>
<body>
  <div class="card">
    <svg class="pour-artwork" viewBox="0 0 290 462" role="img" aria-label="Illustration of wine pouring into a wine glass">
      <defs>
        <linearGradient id="wineTone" x1="0" y1="0" x2="1" y2="1">
          <stop offset="0" stop-color="#b5226a"/>
          <stop offset="1" stop-color="#8c1650"/>
        </linearGradient>
      </defs>
      <rect width="290" height="462" fill="url(#wineTone)"/>
    </svg>
    <div class="edge-band"></div>
    <div class="contact">
      <p class="contact__name">Rosalind Thwaite</p>
      <p class="contact__company">Meridale Wine Collective</p>
      <p class="contact__line">PO Box 738,</p>
      <p class="contact__line">Fenwick Vale</p>
      <p class="contact__line contact__line--gap">South Australia 5187</p>
      <p class="contact__line">Phone: +61 (0)455 982 317</p>
      <p class="contact__line">Email: kvcellars@brightmail.example</p>
    </div>
  </div>
</body>
</html>
```